Homepage design change needed

We're looking for a designer to change the way our homepage looks according to the attached sketch along with the project brief below.
Existing website is: http://www.tallowmere.co.nz
Please download the sketched design from the link below. https://www.parcelvoxa.com/s/k3m9q2x7t4w1z8r/fwdwebsitedesignneeded2.zip
There are 4 images inside the above zip file. front1, 2 & 3 make up the homepage.
page2.jpg is a sketch of what we'd like instead of the current page http://www.tallowmere.co.nz/join-tallowmere.aspx
Requirements
Must have
- The design must keep the following elements the same as the existing website:
- colour scheme
- same width
- same rounded corners/soft edges
- rounded buttons
- the graphics look of the following video brought through into the illustrations http://www.tallowmere.co.nz/help/video.aspx
front1.jpg - there is an illustration (3 boxes with = success! written); please don't design an illustration, simply leave space for a graphic to be put in its place later.
front2 and 3.jpg are to be fully designed as sketched. (again please ignore the illustration with 3 boxes = success!)

```html
<!DOCTYPE html>
<html lang="en">
<head>
<meta charset="utf-8">
<title>Skelvaro – Join</title>
<link href="https://fonts.googleapis.com/css2?family=Source+Sans+3:wght@300;400;600&display=swap" rel="stylesheet">
<style>
:root{
  --blue:#1aa3e8;
  --blue-dark:#1487d0;
  --band:#3fa6ec;
  --border:#7cc6f2;
  --card:#f7f7f7;
  --card-edge:#e2e2e2;
  --text:#4a4a4a;
  --muted:#8a8a8a;
  --page:#f2f2f2;
  --white:#fff;
}
*{box-sizing:border-box;margin:0;padding:0}
html,body{width:1200px;height:1139px;overflow:hidden}
body{position:relative;background:var(--page);font-family:"Source Sans 3",sans-serif;color:var(--text)}
.abs{position:absolute}
a{color:inherit;text-decoration:none}

.site-header{left:94px;top:0;width:1018px;height:149px;background:var(--white);border:1px solid #ddd;border-top:none;border-radius:0 0 18px 18px}
.brand{left:40px;top:28px;font-size:38px;font-weight:400;color:var(--blue);letter-spacing:.5px;display:flex;align-items:center;gap:10px}
.brand-dot{width:14px;height:14px;border-radius:50%;background:var(--blue)}
.top-links{right:30px;top:62px;font-size:16px;color:#666;font-weight:300}
.top-links span{margin:0 7px;color:#999}
.main-nav{left:-1px;top:96px;width:1018px;height:52px;background:var(--band);border-radius:0 0 18px 18px;display:flex;align-items:center;padding-left:57px;font-size:19px;color:var(--white)}
.main-nav span.sep{margin:0 20px;opacity:.7}

.panel{background:var(--white);border:1px solid var(--border);border-radius:22px}
.signup-panel{left:95px;top:180px;width:1017px;height:562px}
.card{background:linear-gradient(#fff,var(--card) 60%);border:2px solid var(--card-edge);border-radius:4px}
.profile-card{left:30px;top:38px;width:516px;height:437px}
.join-card{left:576px;top:38px;width:409px;height:437px}
.card-title{font-size:26px;color:var(--blue);font-weight:400}
.card-sub{font-size:18px;color:var(--blue);font-weight:300}

.tag{height:25px;border:1.5px solid var(--blue);border-radius:5px;background:#fff;font-size:14px;color:#555;display:flex;align-items:center;padding-left:11px;gap:6px}
.tag i{width:12px;height:12px;border:1px solid #bbb;border-radius:2px;display:block}
.photo{width:96px;height:86px;background:#fff;border:1px solid #ddd;border-radius:6px;padding:6px;box-shadow:0 1px 3px rgba(0,0,0,.08)}
.photo div{width:100%;height:100%;border-radius:2px}
.person{font-size:14px;line-height:22px;font-weight:300;color:var(--muted)}
.person b{display:block;font-weight:400;color:#444;font-size:15px}

.field-label{font-size:14px;color:#444}
.field{width:270px;height:29px;border:1px solid #ddd;border-radius:4px;background:#fff}
.btn-next{left:225px;top:377px;width:90px;height:37px;background:linear-gradient(var(--blue),var(--blue-dark));border-radius:5px;color:#fff;font-size:18px;display:flex;align-items:center;justify-content:center;gap:6px}

.footer-panel{left:92px;top:769px;width:1016px;height:400px;border-radius:22px 22px 0 0}
.footer-nav{left:32px;top:35px;width:950px;height:50px;background:linear-gradient(#fff,#f4f4f4);border:2px solid var(--card-edge);border-radius:4px;display:flex;align-items:center;padding-left:20px;font-size:16px;color:var(--blue-dark)}
.footer-nav a{margin-right:22px}
.footer-nav .az{margin-left:46px;font-size:14.5px;word-spacing:3px}
.cat-col{font-size:14.3px;line-height:25px;color:var(--blue-dark);font-weight:300}
.legal{left:37px;top:310px;font-size:14.5px;color:#555}
.legal span{margin:0 7px;color:#999}
.copy{left:35px;top:339px;font-size:13px;color:var(--muted);font-weight:300}
.social{top:311px;width:26px;height:26px;border-radius:3px;background:var(--band)}
</style>
</head>
<body>

<header class="site-header abs">
  <div class="brand abs"><span>skelvaro.co.nz</span><span class="brand-dot"></span></div>
  <nav class="top-links abs"><a href="#">home</a><span>|</span><a href="#">Join</a><span>|</span><a href="#">Contact Us</a></nav>
  <nav class="main-nav abs">
    <a href="#">Search to Hire</a><span class="sep">|</span>
    <a href="#">I want to be hired</a><span class="sep">|</span>
    <a href="#">Employer Services</a><span class="sep">|</span>
    <a href="#">My Skelvaro</a>
  </nav>
</header>

<section class="signup-panel panel abs">
  <div class="profile-card card abs">
    <h2 class="card-title abs" style="left:26px;top:26px">Create your profile now</h2>
    <p class="card-sub abs" style="left:31px;top:64px">We have a profile to suit you</p>

    <div class="tag abs" style="left:29px;top:116px;width:124px"><i></i>Job Seekers</div>
    <div class="tag abs" style="left:29px;top:145px;width:124px"><i></i>Contractors</div>
    <div class="tag abs" style="left:29px;top:174px;width:124px"><i></i>Freelancers</div>
    <div class="tag abs" style="left:29px;top:217px;width:124px"><i></i>Small Business</div>
    <div class="tag abs" style="left:29px;top:246px;width:124px"><i></i>Self Employed</div>
    <div class="tag abs" style="left:29px;top:324px;width:156px"><i></i>Currently working</div>
    <div class="tag abs" style="left:29px;top:353px;width:156px"><i></i>Maintaining Privacy</div>

    <div class="photo abs" style="left:193px;top:112px"><div role="img" aria-label="Profile photo of a member" style="background:linear-gradient(135deg,#8a5a3a,#d9a27a 55%,#3f7fb5)"></div></div>
    <div class="photo abs" style="left:195px;top:211px"><div role="img" aria-label="Profile photo of a member" style="background:linear-gradient(135deg,#9a9a9a,#c98c68 55%,#e6e2dc)"></div></div>
    <div class="photo abs" style="left:197px;top:316px"><div role="img" aria-label="Profile photo of a member" style="background:linear-gradient(135deg,#5a4230,#c7a085 55%,#eceae6)"></div></div>

    <div class="person abs" style="left:307px;top:114px"><b>Person Name</b>Location/State<br>Other Point here</div>
    <div class="person abs" style="left:309px;top:213px"><b>Person Name</b>Location/State<br>Other Point here</div>
    <div class="person abs" style="left:312px;top:318px"><b>Person Name</b>Location/State<br>Other Point here</div>
  </div>

  <div class="join-card card abs">
    <h2 class="card-title abs" style="left:46px;top:21px">Join now (it’s free)</h2>
    <label class="field-label abs" style="left:48px;top:77px">First Name</label>
    <div class="field abs" style="left:46px;top:98px"></div>
    <label class="field-label abs" style="left:48px;top:135px">Last Name</label>
    <div class="field abs" style="left:46px;top:156px"></div>
    <label class="field-label abs" style="left:48px;top:192px">Email address</label>
    <div class="field abs" style="left:46px;top:213px"></div>
    <label class="field-label abs" style="left:48px;top:250px">Skelvaro Name</label>
    <div class="field abs" style="left:45px;top:272px"></div>
    <label class="field-label abs" style="left:48px;top:308px">Password</label>
    <div class="field abs" style="left:46px;top:336px"></div>
    <a class="btn-next abs" href="#">NEXT
      <svg width="8" height="12" viewBox="0 0 8 12"><path d="M0 0L8 6L0 12Z" fill="#fff"/></svg>
    </a>
  </div>
</section>

<footer class="footer-panel panel abs">
  <nav class="footer-nav abs">
    <a href="#">Search to Hire</a><a href="#">I want to be hired</a><a href="#">My Skelvaro</a>
    <span class="az">Profile Directory&nbsp; A B C D E F G H I J K L M N O P Q R S T U V W X Y Z</span>
  </nav>
  <div class="cat-col abs" style="left:42px;top:110px">Call Centre / Customer Services (941)<br>Administration (930)<br>Retail (896)<br>Hospitality / Restaurant (741)<br>Don’t fit in a box? (551)<br>Sales &amp; Marketing (475)</div>
  <div class="cat-col abs" style="left:314px;top:110px">Accounting (273)<br>Transport &amp; Logistics (259)<br>Education / Tuition (229)<br>Manufacturing &amp; Production (198)<br>Children &amp; Babies (178)<br>Entertainment &amp; Events (176)</div>
  <div class="cat-col abs" style="left:559px;top:110px">Tourism (164)<br>Health &amp; Medical (154)<br>Engineering / Construction (147)<br>Publishing (146)<br>Business Growth Services (136)<br>Trades (174)</div>
  <div class="cat-col abs" style="left:783px;top:110px">Financial Services (116)<br>Arts &amp; Crafts (110)<br>Pets (102)<br>Home Help / Domestic Services (89)<br>Design (86)<br>IT &amp; Telecommunications (340)</div>

  <nav class="legal abs"><a href="#">Home</a><span>|</span><a href="#">Join / Sign In</a><span>|</span><a href="#">Contact Us</a><span>|</span><a href="#">Terms and Conditons</a><span>|</span><a href="#">Privacy Policy</a><span>|</span><a href="#">Terms of Use</a></nav>
  <p class="copy abs">Copyright © 2013 Company Name.&nbsp; All right reserved.</p>
  <a class="social abs" href="#" aria-label="Social link" style="left:894px"></a>
  <a class="social abs" href="#" aria-label="Social link" style="left:924px"></a>
  <a class="social abs" href="#" aria-label="Social link" style="left:955px"></a>
</footer>

</body>
</html>
```